I need a SEO-friendly Wordpress website (making sure to style H1, H2, H3, etc correctly) for a Hawaii-based law firm called Meridian Crest Legal Group. Comparable websites include https://trvlaw.example/ and https://www.boultem.example/ for design reference. The current copy on the WelbyCounsel.example website can be used.

Coding

```html
<!DOCTYPE html>
<html lang="en">
<head>
<meta charset="utf-8">
<title>Meridian Crest Legal Group</title>
<link rel="stylesheet" href="https://fonts.googleapis.com/css2?family=Playfair+Display:wght@400;700&family=Poppins:wght@400;500;600&family=Roboto:wght@400;500&display=swap">
<style>
:root{
  --orange:#e0862b;
  --brown:#6e2e1a;
  --brown-dark:#2e150c;
  --ink:#1d1d1d;
  --body:#333;
  --paper:#f2f2f2;
  --header:#f4f6fa;
  --card:rgba(228,210,206,.9);
  --map-light:#ecebe8;
  --map-mid:#dcdcda;
}
*{margin:0;padding:0;box-sizing:border-box}
html,body{width:876px;height:1200px;overflow:hidden}
body{position:relative;font-family:'Poppins',sans-serif;color:var(--body);background:var(--paper)}
.abs{position:absolute}
.topbar{left:0;top:0;width:876px;height:18px;background:var(--orange);color:#fff;font-size:7px;display:flex;justify-content:flex-end;align-items:center;gap:18px;padding-right:168px}
.topbar span{display:flex;align-items:center;gap:6px}
.header{left:0;top:18px;width:876px;height:68px;background:var(--header)}
.brand{left:166px;top:35px}
.brand h1{font-family:'Playfair Display',serif;font-weight:700;font-size:15px;color:var(--ink)}
.brand p{font-size:7.5px;letter-spacing:1px;color:var(--orange);margin-top:3px}
.nav{left:425px;top:48px;display:flex;font-size:7.2px;color:var(--brown);list-style:none}
.nav li{margin-right:15px}
.hero{left:0;top:86px;width:876px;height:248px;background:radial-gradient(ellipse at 40% 45%,#c8822e 0%,#8a3e1c 35%,#6e2e1a 70%)}
.card{left:438px;top:125px;width:255px;height:169px;background:var(--card);padding:11px 10px}
.card h2{font-family:'Playfair Display',serif;font-size:16px;font-weight:700;color:var(--ink);letter-spacing:.5px}
.card h3{font-weight:400;font-size:10px;letter-spacing:1px;color:var(--ink)}
.card p{font-size:7px;margin-top:12px;line-height:1.55;color:var(--ink)}
.card ul{list-style:none;font-size:7.8px;font-weight:500;color:var(--ink);margin-top:11px;line-height:1.75}
.share{left:0;top:140px;width:20px}
.share i{display:block;height:22px}
.about{left:0;top:334px;width:876px;height:298px;background:#fff}
.about-text{left:173px;top:352px;width:285px}
.about-text h2,.practice h2{font-family:'Playfair Display',serif;font-size:17px;font-weight:700;color:var(--ink);letter-spacing:.5px}
.rule{width:18px;height:3px;background:var(--ink);margin-top:5px}
.about-text p{font-size:7.3px;line-height:1.75;margin-top:14px;color:#333}
.btn{left:173px;top:576px;width:100px;height:27px;background:var(--orange);color:#fff;font-size:7.3px;font-weight:500;display:flex;align-items:center;justify-content:center}
.portrait{left:496px;top:346px;width:152px;height:286px;background:linear-gradient(180deg,#e4e4e4,#2b2b2b 35%,#1a1a1a)}
.presence{left:0;top:632px;width:876px;height:118px;background:linear-gradient(90deg,#3a1a0e,#7a4a2a 50%,#3a1a0e);text-align:center;color:#fff}
.presence h2{font-family:'Playfair Display',serif;font-size:17px;font-weight:700;margin-top:15px}
.presence p{font-size:7.6px;font-style:italic;line-height:1.5;width:510px;margin:19px auto 0}
.practice{left:0;top:750px;width:876px;text-align:center}
.practice h2{margin-top:32px}
.practice .rule{margin:5px auto 0}
.area{top:837px;width:110px;text-align:center;font-size:7px;font-weight:500;color:var(--ink);font-family:'Roboto',sans-serif}
.area svg{display:block;margin:0 auto 14px}
.footer-info{left:0;top:956px;width:355px;height:217px;background:var(--brown);color:#fff;font-family:'Roboto',sans-serif;font-size:7.3px;padding:10px 0 0 171px;line-height:1.45}
.footer-info .label{color:#e21b1b;margin-top:10px}
.socials{display:flex;gap:4px;margin-top:12px}
.socials i{width:14px;height:14px;background:#2f6db5}
.contact{left:355px;top:956px;width:167px;height:217px;background:var(--orange);padding:12px 21px 0}
.contact h2{font-family:'Playfair Display',serif;font-size:16px;font-weight:700;color:#fff}
.field{font-family:'Roboto',sans-serif;font-size:6.3px;color:#fff;border-bottom:1px solid rgba(255,255,255,.7);height:15px;margin-top:6px;padding-top:4px}
.field.msg{height:40px}
.submit{margin:18px 0 0 14px;width:100px;height:27px;background:#f7e3e3;color:var(--ink);font-family:'Roboto',sans-serif;font-size:9px;display:flex;align-items:center;justify-content:center}
.map{left:522px;top:956px;width:354px;height:217px;background:linear-gradient(135deg,var(--map-light),var(--map-mid))}
.copyright{left:0;top:1173px;width:876px;height:27px;background:var(--brown-dark);color:#fff;font-size:6.3px;display:flex;align-items:center;justify-content:center}
</style>
</head>
<body>
<div class="abs topbar">
  <span><svg width="8" height="6" viewBox="0 0 8 6"><rect width="8" height="6" fill="#fff"/><path d="M0 0l4 3 4-3" stroke="#e0862b" fill="none" stroke-width=".8"/></svg>clients@welbycounsel.example</span>
  <span><svg width="7" height="7" viewBox="0 0 10 10"><path d="M2 1l2 2-1 1.5a6 6 0 0 0 2.5 2.5L7 6l2 2-1.5 1.5C4 9 1 6 .5 2z" fill="#fff"/></svg>+1.808.555.0148</span>
</div>

<header class="abs header"></header>
<div class="abs brand"><h1>Meridian Crest Legal Group</h1><p>Divorce and Personal Injury Lawyers</p></div>
<ul class="abs nav"><li>HOME</li><li>OUR FIRM</li><li>PRACTICE AREAS</li><li>ATTORNEYS</li><li>BLOG</li><li style="margin-left:2px">CONTACT</li></ul>

<section class="abs hero" role="img" aria-label="Golden statue of Lady Justice holding scales and a sword against a warm brown background"></section>
<div class="abs card">
  <h2>KONA LAWYERS OF MCLG</h2>
  <h3>LEGAL KŌKUA WITH ALOHA.</h3>
  <p>Over 70 years of combined practice, specializing in:</p>
  <ul><li>Personal Injury</li><li>Family &amp; Divorce</li><li>Child Custody</li></ul>
  <p>Dedicated to making sure you receive the care and attention you need.</p>
</div>
<div class="abs share">
  <i style="background:#3b5998"></i><i style="background:#1da1f2"></i><i style="background:#8a9aa5"></i><i style="background:#7f8c95"></i><i style="background:#f26a4f"></i>
</div>

<section class="abs about"></section>
<div class="abs about-text">
  <h2>ABOUT US</h2><div class="rule"></div>
  <p>Lawyers Serving the Big Island and Neighboring Islands</p>
  <p>The experienced attorneys in the Meridian Crest Legal Group’s Kailua Kona, Hawaii office provide clients with a wide range of litigation expertise, including legal claims involving divorce &amp; family, personal injury, toxic exposures, intellectual property, and real estate.</p>
  <p>Our Kona office also offers commercial and hospitality litigation expertise on behalf of a wide variety of clients, including restaurants, hotels, property owners, and many others. We never wish to see our clients go to court, though if there is no other option, you’re in safe hands with our seasoned trial lawyers and the many years of courtroom experience behind them.</p>
</div>
<div class="abs btn">KNOW MORE</div>
<div class="abs portrait" role="img" aria-label="Portrait of an attorney in a dark suit"></div>

<section class="abs presence" role="img" aria-label="Blurred courtroom gavel background">
  <h2>Nationwide Law Firm Presence</h2>
  <p>Kailua Kona serves as the firm’s West Coast headquarters for litigation and representation on behalf of individuals and corporations involved in a wide range of legal matters. The firm and its attorneys are licensed to practice and represent clients in Hawaii, California, Arizona, Texas, and Washington D.C</p>
</section>

<section class="abs practice"><h2>OUR PRACTICE AREA</h2><div class="rule"></div></section>
<div class="abs area" style="left:206px">
  <svg width="50" height="50" viewBox="0 0 50 50"><circle cx="25" cy="25" r="24" fill="none" stroke="#e0862b" stroke-width="1.2"/><path d="M14 25l11-9 11 9M17 23v11h16V23M22 34v-6h6v6" fill="none" stroke="#e0862b" stroke-width="1.4"/></svg>FAMILY &amp; DIVORCE</div>
<div class="abs area" style="left:321px">
  <svg width="50" height="50" viewBox="0 0 50 50"><circle cx="25" cy="25" r="24" fill="none" stroke="#e0862b" stroke-width="1.2"/><path d="M15 16l5 5M20 16l-5 5M26 29l4 4M30 29l-4 4M20 23q6-6 12-2" fill="none" stroke="#e0862b" stroke-width="1.3"/><circle cx="34" cy="20" r="1.8" fill="#e0862b"/><circle cx="18" cy="32" r="1.8" fill="#e0862b"/></svg>CORPORATE &amp; IP</div>
<div class="abs area" style="left:446px">
  <svg width="50" height="50" viewBox="0 0 50 50"><circle cx="25" cy="25" r="24" fill="none" stroke="#e0862b" stroke-width="1.2"/><rect x="19" y="13" width="12" height="24" rx="6" fill="none" stroke="#e0862b" stroke-width="1.3"/><path d="M25 20v10M20 25h10" stroke="#e0862b" stroke-width="1.3"/></svg>PERSONAL INJURY</div>
<div class="abs area" style="left:566px">
  <svg width="50" height="50" viewBox="0 0 50 50"><circle cx="25" cy="25" r="24" fill="none" stroke="#e0862b" stroke-width="1.2"/><path d="M17 21l7-7 5 5-7 7zM24 22l9 9M16 35h16" fill="none" stroke="#e0862b" stroke-width="1.4"/></svg>REAL ESTATE</div>

<footer class="abs footer-info">
  <div>Kona Lawyers of Meridian Crest Legal Group</div>
  <div class="label">Find Us</div>
  <div>41-200 Lanakila Road, Suite 12<br>Kailua Kona, Hawaii 96740.</div>
  <div class="label">Call Us Today</div>
  <div>T: &nbsp;+1.808.555.0148</div>
  <div class="label">Email Us Now</div>
  <div style="font-size:6.5px">clients@welbycounsel.example</div>
  <div class="label">Visit Our Website</div>
  <div style="font-size:6.5px">www.welbycounsel.example</div>
  <div class="socials"><i></i><i></i><i></i><i></i></div>
</footer>
<section class="abs contact">
  <h2>CONTACT US</h2>
  <div class="field" style="margin-top:14px">Name</div>
  <div class="field">Email</div>
  <div class="field">Phone</div>
  <div class="field msg">Message</div>
  <div class="submit">SUBMIT</div>
</section>
<div class="abs map" role="img" aria-label="Street map of Kailua Kona showing the office location"></div>
<div class="abs copyright">Copyright © Meridian Crest Legal Group. All Rights Reserved.</div>
</body>
</html>
```